4K Business Card Design

We need a business card that emphasizes consulting services worldwide. The name of the company is KKKK Consulting Group. We provide consulting services across several industries including but not limited to commodities, telecom, manufacturing, logistics, marketing and operations. We would like to see a creative design that emphasizes the global aspect, including Latin America and US markets, as well the bilingual nature of the service offerings.

The contact information section should include icons to represent the following data:
1) Name, Title and Company Name
2) Mobile Number
3) Skype ID
4) Email
5) Web Page
6) Location

We would like to see a card that emphasizes the worldwide concept. The back of the card should be simple, including only the logo (or a portion of the logo) and the slogan.

We would also like to see business cards in a booklet format. The colors to be used should be the same combination of colors used in the logos attached to this brief.

The logo design and some business card examples from Artful Herd are attached for reference on style and look.

Target Market(s)

International business executives, 45-65 years of age, bilingual

Industry/Entity Type

Marketing

Colors
0792cd
34a7d8
85cae6
ffffff
cee9f5
ecf7fb

Requirements
Must have
• Please follow colors in logo attached.

2) Mobile Number
3) Skype ID
4) Email
5) Web Page
6) Location
Nice to have
• Global concept, consulting profile, diverse industry focus
Should not have
• No black color

```html
<!DOCTYPE html>
<html lang="en">
<head>
<meta charset="utf-8">
<title>KKKK Consulting Group — Business Cards</title>
<link rel="stylesheet" href="https://fonts.googleapis.com/css2?family=Montserrat:wght@600;700&family=Lato:wght@400;700&display=swap">
<style>
  :root {
    --blue-deep: #0572a6;
    --blue: #0792cd;
    --blue-mid: #34a7d8;
    --blue-light: #85cae6;
    --blue-pale: #cee9f5;
    --blue-mist: #ecf7fb;
    --white: #ffffff;
    --backdrop: #eef2f4;
  }
  * { margin: 0; padding: 0; box-sizing: border-box; }
  html, body { width: 1200px; height: 913px; overflow: hidden; }
  body { background: var(--backdrop); position: relative; font-family: "Lato", sans-serif; }

  .card {
    position: absolute;
    width: 540px; height: 309px;
    overflow: hidden;
    box-shadow: 0 10px 28px rgba(5, 60, 90, 0.22);
  }
  .card--front { left: 40px; top: 302px; }
  .card--back { left: 620px; top: 302px; }
  .card__art { position: absolute; inset: 0; width: 100%; height: 100%; }

  .brand-name {
    position: absolute;
    font-family: "Montserrat", sans-serif;
    font-weight: 700;
    line-height: 1.15;
    text-align: center;
  }
  .card--front .brand-name {
    left: 120px; top: 136px; width: 300px;
    font-size: 26px;
    color: var(--blue-mid);
    transform: rotate(-11deg);
  }
  .card--back .brand-name {
    left: 30px; top: 122px; width: 230px;
    font-size: 24px;
    color: var(--white);
  }

  .contact {
    position: absolute; left: 300px; top: 62px; width: 220px;
    color: var(--white);
  }
  .contact__name {
    font-family: "Montserrat", sans-serif; font-weight: 600;
    font-size: 15px; letter-spacing: 0.5px; color: var(--blue-deep);
  }
  .contact__role { font-size: 10px; margin-top: 2px; }
  .contact__company { font-size: 10px; margin-bottom: 8px; }
  .contact__list { list-style: none; }
  .contact__item {
    display: flex; align-items: center; gap: 8px;
    font-size: 11px; height: 17px;
  }
  .contact__icon { width: 12px; height: 12px; flex: none; }
</style>
</head>
<body>

<section class="card card--front" aria-label="Business card front">
  <svg class="card__art" viewBox="0 0 540 309" preserveAspectRatio="none">
    <rect width="540" height="309" fill="var(--blue)"/>
    <polygon points="0,0 540,0 540,40 0,150" fill="var(--blue-light)"/>
    <polygon points="120,0 540,0 540,40 260,97" fill="var(--blue-mid)"/>
    <polygon points="380,0 540,0 540,40" fill="var(--blue)"/>
    <polygon points="0,0 200,0 0,110" fill="var(--blue-pale)"/>
    <polygon points="0,270 540,150 540,309 0,309" fill="var(--blue-deep)"/>
    <polygon points="180,230 540,150 540,309 380,309" fill="var(--blue-mid)"/>
    <polygon points="380,309 540,230 540,309" fill="var(--blue)"/>
    <polygon points="0,270 120,243 200,309 0,309" fill="var(--blue)"/>
    <polygon points="0,150 540,40 540,150 0,270" fill="var(--white)"/>
    <polygon role="img" aria-label="Faint world map behind the company name" points="0,150 540,40 540,150 0,270" fill="var(--blue-mist)" opacity="0.8"/>
  </svg>
  <p class="brand-name">KKKK Consulting Group</p>
</section>

<section class="card card--back" aria-label="Business card back">
  <svg class="card__art" viewBox="0 0 540 309" preserveAspectRatio="none">
    <rect width="540" height="309" fill="var(--white)"/>
    <polygon points="0,95 540,40 540,270 0,215" fill="var(--blue)"/>
    <polygon points="0,95 270,67 270,160 0,215" fill="var(--blue-deep)"/>
    <polygon points="270,160 540,40 540,270" fill="var(--blue-deep)"/>
    <polygon points="270,67 540,40 540,70 270,160" fill="var(--blue-mid)"/>
    <polygon points="0,215 270,160 270,242" fill="var(--blue)"/>
    <rect x="20" y="70" width="250" height="165" fill="var(--blue-mid)" opacity="0.85"/>
    <rect x="270" y="50" width="250" height="185" fill="var(--blue-mid)" opacity="0.85"/>
    <rect role="img" aria-label="Faint world map tint across the panels" x="20" y="50" width="500" height="185" fill="var(--blue-light)" opacity="0.2"/>
    <line x1="270" y1="50" x2="270" y2="235" stroke="var(--white)" stroke-width="1.5"/>
  </svg>
  <p class="brand-name">KKKK Consulting Group</p>
  <div class="contact">
    <p class="contact__name">LENA ORTIZ</p>
    <p class="contact__role">President &amp; CEO</p>
    <p class="contact__company">KKKK Consulting Group, Inc</p>
    <ul class="contact__list">
      <li class="contact__item">
        <svg class="contact__icon" viewBox="0 0 12 12"><rect x="3" y="0.5" width="6" height="11" rx="1" fill="none" stroke="currentColor"/><circle cx="6" cy="9.5" r="0.7" fill="currentColor"/></svg>
        +1 555 014 2290
      </li>
      <li class="contact__item">
        <svg class="contact__icon" viewBox="0 0 12 12"><rect x="0.5" y="2.5" width="11" height="7" fill="none" stroke="currentColor"/><polyline points="0.5,2.5 6,7 11.5,2.5" fill="none" stroke="currentColor"/></svg>
        hello@kkkkmail.com
      </li>
      <li class="contact__item">
        <svg class="contact__icon" viewBox="0 0 12 12"><circle cx="6" cy="6" r="5.5" fill="currentColor"/></svg>
        k4consultinggroup
      </li>
      <li class="contact__item">
        <svg class="contact__icon" viewBox="0 0 12 12"><circle cx="6" cy="6" r="5.3" fill="none" stroke="currentColor"/><ellipse cx="6" cy="6" rx="2.3" ry="5.3" fill="none" stroke="currentColor"/><line x1="0.7" y1="6" x2="11.3" y2="6" stroke="currentColor"/></svg>
        www.kkkkconsult.com
      </li>
      <li class="contact__item">
        <svg class="contact__icon" viewBox="0 0 12 12"><path d="M6 11.5 C3 8 2 6 2 4.3 A4 4 0 0 1 10 4.3 C10 6 9 8 6 11.5Z" fill="currentColor"/><circle cx="6" cy="4.3" r="1.5" fill="var(--blue)"/></svg>
        Cedar Bay, FL
      </li>
    </ul>
  </div>
</section>

</body>
</html>
```